Technology company needs an invitation for a Machine Learning Event

We need a invitation design for a technology company called Corvelane. We specialize on IT Services and Consulting and we're scheduling an Event on Machine Learning and Artificial Intelligence. Machine learning is a method of data analysis that automates analytical model building. It is a branch of artificial intelligence based on the idea that systems can learn from data, identify patterns and make decisions with minimal human intervention. It is the result of algorithmic implementations for data analysts to use. So basically, it provides systems the ability to automatically learn and improve from experience without being explicitly programmed to. Machine learning focuses on the development of computer programs that can access data and use it learn for themselves.

```html
<!DOCTYPE html>
<html lang="en">
<head>
<meta charset="utf-8">
<title>Corvelane – Machine Learning and Artificial Intelligence Invitation</title>
<link rel="stylesheet" href="https://fonts.googleapis.com/css2?family=Open+Sans:wght@400;600;700&display=swap">
<style>
  :root {
    --page-bg: #e9e6e1;
    --navy-deep: #141c5c;
    --navy: #1b2a85;
    --navy-mid: #22389e;
    --dot-blue: #3f8fe0;
    --circuit-blue: #2f7fd0;
    --band-white: #ffffff;
    --band-silver: #c9cbe0;
    --headline: #f5b51d;
    --text-white: #ffffff;
    --brand-dark: #1d1d2b;
    --brand-red: #e0412a;
  }
  * { margin: 0; padding: 0; box-sizing: border-box; }
  html, body {
    width: 1200px; height: 1000px; overflow: hidden;
    background: var(--page-bg);
    font-family: "Open Sans", sans-serif;
  }
  .invitation {
    position: absolute; left: 100px; top: 145px;
    width: 1000px; height: 710px;
    background: radial-gradient(ellipse at 50% 45%, var(--navy-mid) 0%, var(--navy) 55%, var(--navy-deep) 100%);
    overflow: hidden;
    box-shadow: 0 10px 30px rgba(0,0,0,0.25);
  }
  .top-strip { position: absolute; left: 0; top: 0; width: 100%; height: 42px; background: var(--navy-deep); }
  .halftone {
    position: absolute;
    background: radial-gradient(ellipse at center, rgba(63,143,224,0.55), rgba(63,143,224,0) 70%);
  }
  .halftone--left { left: -60px; top: 0; width: 300px; height: 420px; }
  .halftone--right { right: -60px; top: 0; width: 320px; height: 440px; }
  .header-band {
    position: absolute; left: 0; top: 42px; width: 100%; height: 112px;
    background: linear-gradient(90deg, var(--band-silver) 0%, var(--band-white) 22%, var(--band-white) 70%, var(--band-silver) 100%);
    display: flex; flex-direction: column; align-items: center; justify-content: center;
  }
  .brand { display: flex; align-items: center; gap: 8px; }
  .brand-dot { width: 22px; height: 22px; border-radius: 50%; background: var(--brand-red); }
  .brand-name { font-weight: 700; font-size: 26px; color: var(--brand-dark); letter-spacing: 0.5px; }
  .brand-tagline { font-size: 10px; font-weight: 600; color: var(--brand-dark); letter-spacing: 0.3px; margin-top: 2px; }
  .headline {
    position: absolute; top: 190px; width: 100%; text-align: center;
    color: var(--headline); font-weight: 700; font-size: 40px; line-height: 50px;
  }
  .intro {
    position: absolute; top: 300px; left: 90px; width: 820px; text-align: center;
    color: var(--text-white); font-weight: 700; font-size: 13.5px; line-height: 33px; text-transform: uppercase;
  }
  .circuit {
    position: absolute; left: 200px; top: 440px; width: 600px; height: 270px;
    background: radial-gradient(ellipse at 50% 40%, rgba(47,127,208,0.45), rgba(47,127,208,0) 70%);
  }
  .side-note {
    position: absolute; top: 575px; width: 240px;
    color: var(--text-white); font-size: 13px; line-height: 18px; text-align: center;
  }
  .side-note--left { left: 85px; }
  .side-note--right { right: 80px; }
</style>
</head>
<body>
  <main class="invitation">
    <div class="halftone halftone--left" role="img" aria-label="Blue halftone dot pattern"></div>
    <div class="halftone halftone--right" role="img" aria-label="Blue halftone dot pattern"></div>
    <div class="top-strip"></div>
    <header class="header-band">
      <div class="brand">
        <span class="brand-dot"></span>
        <span class="brand-name">CORVELANE</span>
      </div>
      <div class="brand-tagline">IT CONSULTING AND SERVICES</div>
    </header>
    <h1 class="headline">MACHINE LEARNING AND<br>ARTIFICIAL INTELLIGENCE.</h1>
    <div class="circuit" role="img" aria-label="Glowing blue circuit board traces"></div>
    <p class="intro">Lorem ipsum dolor sit amet, consectetuer adipiscing elit, sed diam nonummy nibh euismod tincidunt ut laoreet dolore magna aliquam erat volutpat. Ut wisi enim ad minim veniam, quis nostrud exerci tation ullamcorper suscipit lobortis nisl ut aliquip ex ea commodo consequat. Duis autem vel eum iriure dolor in hendrerit in vulputate velit esse molestie consequat, vel illum dolore eu feugiat nulla facilisis at vero eros et accumsan et iusto odio dignissim qui blandit praesent luptatum zzril delenit augue duis dolore te feugait nulla facilisi.</p>
    <p class="side-note side-note--left">Lorem ipsum dolor sit amet, consectetuer adipiscing elit, sed diam nonummy nibh euismod tincidunt ut laoreet dolore magna aliquam erat volutpat.</p>
    <p class="side-note side-note--right">Lorem ipsum dolor sit amet, consectetuer adipiscing elit, sed diam nonummy nibh euismod tincidunt ut laoreet dolore magna aliquam erat volutpat.</p>
  </main>
</body>
</html>
```